Business cards for the RL Group

We are looking for a template for our new business cards for our company that we can edit ourselves.
You will find our company colors in the logo. the logo on the back and on the front
first name Last Name
position
E-mail address
mobile number
landline number
Companies we have 2 RL Sicherheit GmbH and RL Services GmbH
address
Lindenbergweg 42
22459 Hamburg
www.rlgruppe-nord.de

Something modern, simple but professional

if you have any questions, bring it on.

Sicherheit

Steht in der Beschreibung

F0912C
F2A743
F7CA91
FBE8D2
FDF5EE

• recognition value
• professional
• Playful

```html
<!DOCTYPE html>
<html lang="de">
<head>
<meta charset="utf-8">
<title>RL Gruppe – Visitenkarten</title>
<link rel="stylesheet" href="https://fonts.googleapis.com/css2?family=Anton&family=Open+Sans:wght@400;700&display=swap">
<style>
  :root {
    --bg-light: #c3c3c8;
    --bg-dark: #7e828b;
    --card-dark: #5c5c5c;
    --card-light: #ffffff;
    --ink: #58595b;
    --orange: #f47b0c;
    --rule: #b8b8b8;
  }
  html, body {
    margin: 0;
    width: 1200px;
    height: 1000px;
    overflow: hidden;
  }
  body {
    position: relative;
    background: linear-gradient(215deg, var(--bg-light) 0%, #a2a4ab 50%, var(--bg-dark) 100%);
    font-family: "Open Sans", sans-serif;
  }
  .card {
    position: absolute;
    box-shadow: 0 1px 3px rgba(0,0,0,0.18);
  }
  .card-back {
    left: 85px; top: 345px; width: 466px; height: 301px;
    background: var(--card-dark);
  }
  .card-front {
    left: 653px; top: 352px; width: 465px; height: 303px;
    background: var(--card-light);
  }
  .brand {
    position: absolute;
    display: flex;
    align-items: center;
    gap: 12px;
    font-family: "Open Sans", sans-serif;
    font-weight: 700;
    letter-spacing: 1px;
    white-space: nowrap;
  }
  .brand-mark {
    width: 18px; height: 18px;
    border-radius: 50%;
    background: var(--orange);
    flex: none;
  }
  .card-back .brand {
    left: 50%; top: 150px;
    transform: translate(-50%, -50%);
    font-size: 38px;
    color: #ffffff;
  }
  .card-front .brand {
    left: 116px; top: 152px;
    transform: translate(-50%, -50%);
    font-size: 30px;
    color: var(--ink);
  }
  .web {
    position: absolute;
    left: 0; right: 0; top: 266px;
    display: flex; justify-content: center; align-items: center; gap: 6px;
    color: #ffffff;
    font-size: 14px;
    letter-spacing: 0.4px;
  }
  .divider {
    position: absolute;
    left: 232px; top: 30px;
    width: 1px; height: 246px;
    background: var(--rule);
  }
  .person {
    position: absolute;
    left: 261px; top: 89px;
  }
  .person-name {
    font-family: "Anton", sans-serif;
    font-size: 19px;
    color: var(--ink);
    line-height: 1;
    margin: 0;
  }
  .person-position {
    margin: 14px 0 0;
    font-weight: 700;
    font-size: 11.5px;
    letter-spacing: 2.4px;
    color: var(--orange);
  }
  .contact {
    position: absolute;
    left: 261px; top: 164px;
    margin: 0; padding: 0;
    list-style: none;
    font-size: 12.5px;
    color: var(--ink);
    line-height: 17px;
  }
  .contact li {
    display: flex;
    align-items: flex-start;
    gap: 8px;
  }
  .contact li.address { margin-top: 6px; gap: 7px; }
  .contact svg { flex: none; margin-top: 3px; }
</style>
</head>
<body>
  <section class="card card-back" aria-label="Rückseite">
    <div class="brand"><span class="brand-mark"></span>RL GRUPPE</div>
    <div class="web">
      <svg width="12" height="12" viewBox="0 0 12 12" aria-hidden="true">
        <circle cx="6" cy="6" r="5" fill="none" stroke="#f47b0c" stroke-width="1.3"/>
        <ellipse cx="6" cy="6" rx="2.2" ry="5" fill="none" stroke="#f47b0c" stroke-width="1"/>
        <line x1="1" y1="6" x2="11" y2="6" stroke="#f47b0c" stroke-width="1"/>
      </svg>
      <span>rlgruppe-nord.de</span>
    </div>
  </section>

  <section class="card card-front" aria-label="Vorderseite">
    <div class="brand"><span class="brand-mark"></span>RL GRUPPE</div>
    <div class="divider"></div>
    <div class="person">
      <p class="person-name">First Name Last Name</p>
      <p class="person-position">POSITION</p>
    </div>
    <ul class="contact">
      <li>
        <svg width="12" height="12" viewBox="0 0 12 12" aria-hidden="true">
          <path d="M2.5 1 L4.5 1 L5.2 3.6 L4 4.6 C4.7 6.1 5.9 7.3 7.4 8 L8.4 6.8 L11 7.5 L11 9.5 C11 10.3 10.3 11 9.5 11 C5 11 1 7 1 2.5 C1 1.7 1.7 1 2.5 1 Z" fill="#f47b0c"/>
        </svg>
        <span>+49 40 555 0192 47</span>
      </li>
      <li>
        <svg width="13" height="10" viewBox="0 0 13 10" aria-hidden="true">
          <rect x="0" y="0.5" width="13" height="9" fill="#f47b0c"/>
          <path d="M0.5 1 L6.5 5.5 L12.5 1" fill="none" stroke="#ffffff" stroke-width="1.1"/>
        </svg>
        <span>info@services-rl.de</span>
      </li>
      <li class="address">
        <svg width="10" height="14" viewBox="0 0 10 14" aria-hidden="true">
          <path d="M5 0 C2.2 0 0 2.2 0 5 C0 8.5 5 14 5 14 C5 14 10 8.5 10 5 C10 2.2 7.8 0 5 0 Z" fill="#f47b0c"/>
          <circle cx="5" cy="5" r="1.8" fill="#ffffff"/>
        </svg>
        <span>RL Services GmbH<br>Lindenbergweg 42<br>22459 Hamburg</span>
      </li>
    </ul>
  </section>
</body>
</html>
```